Vandrel Group — Business Card Design Brief
Overview
Design a double-sided business card for Vandrel Group that highlights our two service arms: Vandrel Communications (telecommunications) and Vandrel Energy (business energy solutions). The card should feel smart and stand out when handed to clients.

Objectives
Showcase our areas of specialty clearly.
Reflect the overall Vandrel / Vandrel Group brand while acknowledging both arms.
Explore using both logos (Communications + Energy) or one unified logo, depending on the design.

Deliverables
One double-sided business card design (front + back).

Content & Copy
Front (preferred): Logo: Vandrel / Vandrel Group
Descriptor: Business Communications | Business Energy
Back:My contact details and company details
Core products: Business Mobile • Telephony • Internet • Business Energy Solutions

Brand & Visual Direction
We have a group logo currently tailored more toward telecoms, plus a separate Vandrel Energy logo.
Please explore layouts that use both logos or just one, whichever works best.
Color: I wouldn't mind seeing an option using our the Blue/Purple gradient from our website (vandrel-example.co.uk), but also open to non-gradient approaches and other colours..

Overall look: Smart, modern, and distinctive.
Format & Print Specs
Double-sided business card format. (Use a standard size

Must-Haves
Front: Vandrel wording or Vandrel Group wording with atleast 1 logo also on front “Business Communications | Business Energy.”

Back: Contact + company details and core products.
A design that stands out while remaining professional.

Nice-to-Have Options
A gradient version using our site’s Blue/Purple gradient.
A non-gradient version.
A dual-logo treatment versus a single-logo treatment.

Thanks
Dominic

```html
<!DOCTYPE html>
<html lang="en">
<head>
<meta charset="utf-8">
<title>Vandrel Group — Business Card</title>
<link rel="stylesheet" href="https://fonts.googleapis.com/css2?family=Montserrat:wght@400;700&family=Poppins:wght@600;700&family=EB+Garamond:wght@400&display=swap">
<style>
  :root {
    --backdrop: #9a9a9a;
    --card: #1c1462;
    --white: #ffffff;
    --green: #3fae0a;
    --blue: #0aa2dc;
    --blue-deep: #1466d8;
  }
  * { margin: 0; padding: 0; box-sizing: border-box; }
  html, body { width: 1200px; height: 1059px; overflow: hidden; }
  body { background: var(--backdrop); position: relative; }

  .card {
    position: absolute;
    background: var(--card);
    border-radius: 29px;
    overflow: hidden;
    box-shadow: 0 10px 22px rgba(0,0,0,0.35);
    color: var(--white);
  }
  .card--front { left: 252px; top: 88px; width: 724px; height: 415px; }
  .card--back { left: 253px; top: 566px; width: 711px; height: 407px; }

  /* Front */
  .brand-mark { position: absolute; left: 0; top: 0; width: 724px; height: 210px; }
  .brand-mark__dot {
    position: absolute; left: 570px; top: 44px;
    width: 100px; height: 100px; border-radius: 50%;
    background: var(--green);
  }
  .brand-mark__name {
    position: absolute; right: 48px; top: 146px;
    font: 700 42px/1 "Poppins", sans-serif;
    letter-spacing: 0.5px;
    color: var(--white);
  }

  .person__name {
    position: absolute; left: 47px; top: 186px;
    font: 700 27px/1 "Montserrat", sans-serif;
    color: var(--green);
  }
  .person__role {
    position: absolute; left: 46px; top: 225px;
    font: 400 18px/1 "EB Garamond", serif;
  }
  .divider {
    position: absolute; left: 47px; top: 268px;
    width: 633px; height: 1.5px; background: var(--white);
  }

  .contact { position: absolute; left: 44px; top: 286px; list-style: none; }
  .contact__item {
    display: flex; align-items: center; gap: 11px;
    height: 33.5px;
    font: 400 19px/1 "Montserrat", sans-serif;
  }
  .contact__icon { width: 19px; height: 19px; flex: none; fill: var(--blue); }

  .services {
    position: absolute; right: 48px; top: 292px;
    text-align: right; list-style: none;
    font: 600 19px/28px "Poppins", sans-serif;
  }

  .stripe { position: absolute; left: 0; bottom: 0; width: 724px; height: 12px; }

  /* Back */
  .group-title {
    position: absolute; left: 0; right: 0; top: 46px;
    text-align: center;
    font: 700 55px/1 "Poppins", sans-serif;
  }
  .group-mark__dot {
    position: absolute; left: 292px; top: 138px;
    width: 124px; height: 124px; border-radius: 50%;
    background: var(--blue-deep);
  }
  .group-mark__name {
    position: absolute; left: 0; right: 0; top: 274px;
    text-align: center;
    font: 700 58px/1 "Poppins", sans-serif;
    letter-spacing: 0.5px;
  }
</style>
</head>
<body>

<section class="card card--front" aria-label="Card front">
  <div class="brand-mark">
    <span class="brand-mark__dot" aria-hidden="true"></span>
    <span class="brand-mark__name">VANDREL</span>
  </div>

  <h1 class="person__name">Marcus Hale</h1>
  <p class="person__role">Owner</p>
  <div class="divider"></div>

  <ul class="contact">
    <li class="contact__item">
      <svg class="contact__icon" viewBox="0 0 24 24" aria-hidden="true"><path d="M6.6 10.8a15.1 15.1 0 0 0 6.6 6.6l2.2-2.2a1 1 0 0 1 1-.25 11.4 11.4 0 0 0 3.6.57 1 1 0 0 1 1 1V20a1 1 0 0 1-1 1A17 17 0 0 1 3 4a1 1 0 0 1 1-1h3.5a1 1 0 0 1 1 1c0 1.25.2 2.45.57 3.6a1 1 0 0 1-.25 1z"/></svg>
      044-000 555 0142
    </li>
    <li class="contact__item">
      <svg class="contact__icon" viewBox="0 0 24 24" aria-hidden="true"><path d="M2 5h20v2l-10 6L2 7z M2 9l10 6 10-6v10H2z"/></svg>
      hello@vandrel-mail.co.uk
    </li>
    <li class="contact__item">
      <svg class="contact__icon" viewBox="0 0 24 24" aria-hidden="true"><circle cx="12" cy="12" r="10"/><path d="M7 6c2 1 3 3 2 5s1 3 3 3-1 4 1 5M15 4c-1 2 1 3 3 3" stroke="#1c1462" stroke-width="1.6" fill="none"/></svg>
      www.vandrel-example.co.uk
    </li>
  </ul>

  <ul class="services">
    <li>• Business Mobile</li>
    <li>• Telephony • Internet</li>
    <li>• Business Energy Solutions</li>
  </ul>

  <svg class="stripe" viewBox="0 0 724 12" preserveAspectRatio="none" aria-hidden="true">
    <polygon points="0,0 358,0 362,12 0,12" fill="var(--blue)"/>
    <polygon points="362,0 724,0 724,12 367,12" fill="var(--green)"/>
  </svg>
</section>

<section class="card card--back" aria-label="Card back">
  <h2 class="group-title">Vandrel Group</h2>
  <span class="group-mark__dot" aria-hidden="true"></span>
  <p class="group-mark__name">VANDREL</p>
</section>

</body>
</html>
```